Business card design Brightvane

We need a business card for BRIGHTvane aimport and distribution company which sells personnel weight lifting accessories, mainly the dorvel brand of product using our current logo. This design should represent class and a ruggard feel.

Target Market(s)

Weight lifters, crossfitters and other lifting sports

Industry/Entity Type

Weight

Contact Information for Business Card

BRIGHTvane, Owen Palfrey, Cell: 027 918 603, Email: brightvane@mailnest.co.nz, www.brightvane.co.nz

Requirements
Nice to have
• a good looking business card

```html
<!DOCTYPE html>
<html lang="en">
<head>
<meta charset="utf-8">
<title>Brightvane – Business Card</title>
<link rel="stylesheet" href="https://fonts.googleapis.com/css2?family=Arimo:wght@400&family=Exo+2:ital,wght@0,800;1,800&display=swap">
<style>
  :root {
    --paper: #f1f1f1;
    --brand-blue: #005596;
    --ink-dark: #231a0b;
    --text-light: #ffffff;
  }
  html, body {
    margin: 0;
    padding: 0;
    overflow: hidden;
    background: var(--paper);
  }
  .card {
    position: relative;
    width: 1200px;
    height: 694px;
    background: var(--paper);
    overflow: hidden;
    font-family: "Arimo", Arial, sans-serif;
  }
  .holder-name {
    position: absolute;
    right: 72px;
    top: 76px;
    margin: 0;
    font-family: "Exo 2", sans-serif;
    font-style: italic;
    font-weight: 800;
    font-size: 33px;
    letter-spacing: 3px;
    color: var(--ink-dark);
    text-transform: uppercase;
  }
  .wordmark {
    position: absolute;
    left: 180px;
    top: 190px;
    display: flex;
    align-items: center;
    gap: 34px;
  }
  .wordmark-square {
    width: 120px;
    height: 120px;
    background: var(--brand-blue);
  }
  .wordmark-name {
    margin: 0;
    font-family: "Exo 2", sans-serif;
    font-weight: 800;
    font-size: 108px;
    line-height: 1;
    letter-spacing: 2px;
    color: var(--ink-dark);
  }
  .stripes {
    position: absolute;
    left: 0;
    top: 0;
  }
  .stripe-dark { fill: var(--ink-dark); }
  .stripe-blue { fill: var(--brand-blue); }
  .contact {
    position: absolute;
    margin: 0;
    color: var(--text-light);
    font-size: 36px;
    line-height: 1;
  }
  .contact-cell { left: 74px; top: 537px; }
  .contact-email { left: 74px; top: 587px; }
  .contact-web { right: 75px; top: 587px; }
</style>
</head>
<body>
  <main class="card">
    <p class="holder-name">Owen Palfrey</p>

    <div class="wordmark">
      <div class="wordmark-square" aria-hidden="true"></div>
      <h1 class="wordmark-name">BRIGHTVANE</h1>
    </div>

    <svg class="stripes" width="1200" height="694" viewBox="0 0 1200 694" aria-hidden="true">
      <path class="stripe-dark" d="M46 460 H684 V539 H1153 V556 H665 V477 H46 Z"/>
      <path class="stripe-blue" d="M46 496 H643 V575 H1153 V647 H46 Z"/>
    </svg>

    <p class="contact contact-cell">Cell: 027 918 603</p>
    <p class="contact contact-email">Email: brightvane@mailnest.co.nz</p>
    <p class="contact contact-web">www.brightvane.co.nz</p>
  </main>
</body>
</html>
```